Edutainment company need help with Squarespace design

Need help completing website design for a hybrid education and entertainment company called "Novaflickerium". The website will be based through Squarespace. A lot has been done, but need help to make look more consistent with branding and dynamic. Attached is brand kit already created by wonderful designer. Just want help keeping a professional look.

```html
<!DOCTYPE html>
<html lang="en">
<head>
<meta charset="utf-8">
<title>Novaflickerium — Hybrid Education and Entertainment</title>
<link rel="stylesheet" href="https://fonts.googleapis.com/css2?family=Luckiest+Guy&family=Poppins:ital,wght@0,400;0,500;0,600;1,400&display=swap">
<style>
:root{
  --cream:#fdeed8;
  --sand:#ede1c9;
  --ink:#1d1b17;
  --red:#c8321e;
  --yellow:#f8b531;
  --purple:#5b2a91;
  --purple-deep:#4a2278;
  --teal:#1f6a8c;
  --orange:#e8792a;
  --white:#ffffff;
  --text:#2a2724;
  --display:'Luckiest Guy', 'Arial Black', sans-serif;
  --body:'Poppins', Arial, sans-serif;
}
*{box-sizing:border-box;margin:0;padding:0}
html,body{width:1200px;height:4988px;overflow:hidden}
body{position:relative;background:var(--cream);font-family:var(--body);color:var(--text)}
.abs{position:absolute}
.display{font-family:var(--display);font-weight:400;letter-spacing:1px;line-height:1}
.btn{position:absolute;display:flex;align-items:center;justify-content:center;background:var(--yellow);color:var(--white);font-family:var(--display);font-size:22px;letter-spacing:1.5px;text-decoration:none;padding-top:4px}
.body-text{font-size:14.5px;line-height:23px;color:var(--text)}
.photo{position:absolute}
.doodle{position:absolute;border-radius:50%}

/* Hero */
.hero{position:absolute;left:0;top:0;width:1200px;height:652px;background:linear-gradient(110deg,#3c4a3f 0%,#6b6a66 40%,#8b8178 65%,#4f4b47 100%)}
.hero::after{content:"";position:absolute;inset:0;background:rgba(20,18,16,.35)}
.nav a{position:absolute;top:72px;font-family:var(--display);font-size:15px;color:var(--white);text-decoration:none;letter-spacing:1px;z-index:2}
.nav .current{border:2px solid var(--yellow);color:var(--yellow);padding:5px 8px 3px;top:64px}
.brand{position:absolute;z-index:2;font-family:var(--display);color:var(--yellow);letter-spacing:1px}
.hero-title{position:absolute;top:285px;left:0;width:1200px;text-align:center;font-size:78px;color:var(--white);z-index:2}
.hero-sub{position:absolute;top:358px;left:300px;width:600px;text-align:center;font-size:33px;font-weight:500;line-height:37px;color:var(--white);z-index:2}
.dots{position:absolute;top:602px;left:568px;display:flex;gap:8px;z-index:2}
.dots span{width:10px;height:10px;border-radius:50%;background:var(--white)}
.dots span:first-child{background:var(--red)}

.section-title{position:absolute;left:0;width:1200px;text-align:center;font-size:46px;color:var(--ink)}

/* About */
.pillar{position:absolute;top:806px;width:340px;text-align:center}
.pillar .icon{width:84px;height:84px;border-radius:50%;margin:0 auto;display:flex;align-items:center;justify-content:center}
.pillar h3{font-family:var(--display);font-weight:400;color:var(--red);font-size:25px;margin-top:42px;letter-spacing:1px}
.pillar p{font-size:14px;line-height:23px;margin-top:14px}

/* Programs */
.programs{position:absolute;left:0;top:1271px;width:1200px;height:577px;background:var(--sand)}
.program{position:absolute;top:1418px;width:243px}
.program .photo{position:relative;width:243px;height:184px}
.program h3{font-family:var(--display);font-weight:400;color:var(--red);font-size:20px;line-height:26px;margin-top:22px;letter-spacing:1px}
.program p{font-size:13.5px;line-height:22px;margin-top:10px}

/* Feature panels */
.panel{position:absolute;background:var(--white);padding:0 34px}
.panel h2{font-family:var(--display);font-weight:400;font-size:44px;line-height:46px;color:var(--ink);letter-spacing:1px}

/* Testimonial */
.reviews{position:absolute;left:0;top:3063px;width:1200px;height:536px;background:linear-gradient(90deg,#c9b9a6 0%,#d8c7b3 28%,var(--purple-deep) 42%,var(--purple) 100%)}
.reviews h2{position:absolute;left:617px;top:112px;font-family:var(--display);font-weight:400;font-size:44px;color:var(--white);letter-spacing:1px}
.reviews blockquote{position:absolute;left:617px;top:165px;width:510px;font-style:italic;font-size:18.5px;line-height:34px;color:var(--white)}
.reviews cite{position:absolute;left:617px;top:310px;font-style:normal;font-family:var(--display);font-size:21px;color:var(--yellow);letter-spacing:1px}

/* Blog */
.post{position:absolute;top:3754px;width:330px}
.post .photo{position:relative;width:330px;height:209px}
.post h3{font-family:var(--display);font-weight:400;color:var(--red);font-size:20px;margin-top:36px;letter-spacing:1px}
.post p{font-size:13.5px;line-height:26px;margin-top:4px}

/* CTA */
.cta{position:absolute;left:0;top:4174px;width:1200px;height:441px;background:var(--ink);text-align:center}
.cta h2{position:absolute;top:104px;left:0;width:1200px;font-family:var(--display);font-weight:400;font-size:44px;line-height:48px;color:var(--white);letter-spacing:1.5px}
.cta p{position:absolute;top:200px;left:180px;width:840px;font-size:18.5px;line-height:33px;color:var(--white)}

/* Footer */
.footer h4{position:absolute;top:4696px;font-family:var(--display);font-weight:400;font-size:19px;color:var(--ink);letter-spacing:1px}
.footer ul{position:absolute;top:4736px;left:575px;list-style:none}
.footer li{font-size:13px;line-height:32px}
.footer li a{color:var(--text);text-decoration:none}
.contact p{position:absolute;left:882px;font-size:13px;line-height:25px}
.social{position:absolute;left:882px;top:4861px;display:flex;gap:14px}
.social span{width:20px;height:20px;border-radius:50%;background:var(--purple)}
.copyright{position:absolute;left:74px;top:4850px;width:200px;text-align:center;font-size:13px;line-height:25px}
</style>
</head>
<body>

<!-- Hero -->
<header class="hero" role="img" aria-label="Classroom photo of a smiling teacher with pupils gathered around a whiteboard"></header>
<nav class="nav">
  <a class="current" href="#" style="left:79px">Home</a>
  <a href="#" style="left:182px">About Us</a>
  <a href="#" style="left:306px">Programs</a>
  <a href="#" style="left:790px">Testimonials</a>
  <a href="#" style="left:948px">Blog</a>
  <a href="#" style="left:1030px">Contact Us</a>
</nav>
<div class="brand" style="left:480px;top:66px;width:240px;text-align:center;font-size:26px">Novaflickerium</div>
<h1 class="hero-title display">Novaflickerium</h1>
<p class="hero-sub">We are a a hybrid education and entertainment.</p>
<a class="btn" href="#" style="left:495px;top:462px;width:209px;height:58px">Learn More</a>
<div class="dots"><span></span><span></span><span></span><span></span></div>

<!-- About -->
<div class="doodle" style="left:44px;top:628px;width:40px;height:60px;border:6px solid var(--teal);border-left-color:transparent;background:none" role="img" aria-label="Swirl doodle"></div>
<div class="doodle" style="left:1020px;top:640px;width:120px;height:40px;border-radius:8px;background:var(--red)" role="img" aria-label="Paper plane doodle"></div>
<h2 class="section-title display" style="top:716px">About Us</h2>

<div class="pillar" style="left:70px">
  <div class="icon" style="background:var(--teal)"><svg width="44" height="36" viewBox="0 0 44 36" fill="none" stroke="#fff" stroke-width="2"><rect x="4" y="6" width="36" height="22" rx="2"/><path d="M10 22l8-8 6 6 10-10"/><path d="M16 34h12"/></svg></div>
  <h3>Mission</h3>
  <p>Nemo enim ipsam voluptatem quia voluptas sit aspernatur aut odit aut fugit, sed quia consequuntur magni dolores.</p>
</div>
<div class="pillar" style="left:430px">
  <div class="icon" style="background:var(--purple)"><svg width="44" height="40" viewBox="0 0 44 40" fill="none" stroke="#fff" stroke-width="2"><circle cx="22" cy="12" r="5"/><circle cx="10" cy="17" r="4"/><circle cx="34" cy="17" r="4"/><path d="M12 34c0-7 4-12 10-12s10 5 10 12"/><path d="M3 33c0-5 3-8 7-8"/><path d="M41 33c0-5-3-8-7-8"/></svg></div>
  <h3>Vision</h3>
  <p>Nemo enim ipsam voluptatem quia voluptas sit aspernatur aut odit aut fugit, sed quia consequuntur magni dolores.</p>
</div>
<div class="pillar" style="left:790px">
  <div class="icon" style="background:var(--yellow)"><svg width="40" height="40" viewBox="0 0 40 40" fill="none" stroke="#fff" stroke-width="2"><rect x="8" y="4" width="24" height="32" rx="2"/><path d="M13 12h14M13 18h14M13 24h9"/><circle cx="28" cy="30" r="5"/></svg></div>
  <h3>Our Story</h3>
  <p>Nemo enim ipsam voluptatem quia voluptas sit aspernatur aut odit aut fugit, sed quia consequuntur magni dolores.</p>
</div>
<a class="btn" href="#" style="left:495px;top:1113px;width:209px;height:58px">Learn More</a>
<div class="doodle" style="left:400px;top:1200px;width:80px;height:80px;background:var(--red)" role="img" aria-label="Star doodle"></div>
<div class="doodle" style="left:1060px;top:1210px;width:100px;height:90px;background:var(--yellow)" role="img" aria-label="Light bulb doodle"></div>

<!-- Programs -->
<section class="programs"></section>
<div class="doodle" style="left:14px;top:1330px;width:60px;height:70px;border-radius:12px;background:var(--purple)" role="img" aria-label="Music note doodle"></div>
<h2 class="section-title display" style="top:1342px">Programs</h2>
<article class="program" style="left:74px">
  <div class="photo" role="img" aria-label="Teacher and young children playing on a classroom floor" style="background:linear-gradient(135deg,#8a6a52,#c9a27e,#4f6d5a)"></div>
  <h3>Edutainment<br>Shows</h3>
  <p>Nemo enim ipsam voluptatem quia voluptas sit aspernatur aut odit aut fugit, sed quia conse quuntur magni dolores.</p>
</article>
<article class="program" style="left:344px">
  <div class="photo" role="img" aria-label="Adults and children working together at a table in a workshop" style="background:linear-gradient(135deg,#6a4a3a,#b78d6a,#d9b58c)"></div>
  <h3>Courses<br>&amp; Workshops</h3>
  <p>Nemo enim ipsam voluptatem quia voluptas sit aspernatur aut odit aut fugit, sed quia conse quuntur magni dolores.</p>
</article>
<article class="program" style="left:614px">
  <div class="photo" role="img" aria-label="Children looking at a tablet together in class" style="background:linear-gradient(135deg,#4a6a9a,#a8bcd6,#e3d6c4)"></div>
  <h3>Digital<br>Content</h3>
  <p>Nemo enim ipsam voluptatem quia voluptas sit aspernatur aut odit aut fugit, sed quia conse quuntur magni dolores.</p>
</article>
<article class="program" style="left:884px">
  <div class="photo" role="img" aria-label="Presenter speaking to an audience in front of a large screen" style="background:linear-gradient(135deg,#1c2a4a,#2e4a78,#5a7ab0)"></div>
  <h3>Events &amp;<br>Experiences</h3>
  <p>Nemo enim ipsam voluptatem quia voluptas sit aspernatur aut odit aut fugit, sed quia conse quuntur magni dolores.</p>
</article>
<div class="doodle" style="left:742px;top:1790px;width:100px;height:90px;background:var(--red)" role="img" aria-label="Star doodle"></div>
<div class="doodle" style="left:28px;top:1820px;width:66px;height:80px;border:7px solid var(--red);background:none" role="img" aria-label="Swirl doodle"></div>

<!-- Why choose -->
<div class="photo" role="img" aria-label="Cheerful teacher with arms raised at a desk in front of a chalkboard" style="left:74px;top:1921px;width:599px;height:500px;background:linear-gradient(120deg,#1f3a30 0%,#3d5a4a 45%,#9eb3d6 70%,#d9cfc2 100%)"></div>
<div class="panel" style="left:613px;top:1921px;width:511px;height:385px">
  <h2 style="margin-top:64px">Why Choose<br>Novaflickerium?</h2>
  <p class="body-text" style="margin-top:20px">Nemo enim ipsam voluptatem quia voluptas sit aspernatur aut odit aut fugit, sed quia consequuntur magni dolores porro quisquam est, qui dolorem ipsum quia dolor sit amet, consectetur, adipisci velit.</p>
</div>
<a class="btn" href="#" style="left:648px;top:2194px;width:209px;height:58px">Learn More</a>

<!-- Who we serve -->
<div class="photo" role="img" aria-label="Mother and daughter sharing a laptop on a leather sofa" style="left:526px;top:2475px;width:598px;height:499px;background:linear-gradient(120deg,#5a3a2a 0%,#7a5038 40%,#4a6a9a 75%,#2e3e5e 100%)"></div>
<div class="panel" style="left:74px;top:2475px;width:510px;height:383px">
  <h2 style="margin-top:68px">Who We Serve</h2>
  <p class="body-text" style="margin-top:22px">Nemo enim ipsam voluptatem quia voluptas sit aspernatur aut odit aut fugit, sed quia consequuntur magni dolores porro quisquam est, qui dolorem ipsum quia dolor sit amet, consectetur, adipisci velit.</p>
</div>
<a class="btn" href="#" style="left:106px;top:2730px;width:209px;height:58px">Learn More</a>
<div class="doodle" style="left:50px;top:3000px;width:50px;height:70px;border:6px solid var(--teal);border-left-color:transparent;background:none" role="img" aria-label="Swirl doodle"></div>
<div class="doodle" style="left:1040px;top:3010px;width:120px;height:50px;border-radius:8px;background:var(--red)" role="img" aria-label="Paper plane doodle"></div>

<!-- Testimonial -->
<section class="reviews">
  <div class="photo" role="img" aria-label="Smiling young girl resting on a green exercise ball" style="left:0;top:0;width:520px;height:536px;background:linear-gradient(100deg,#b8a48e 0%,#cdb8a2 45%,#6ca24a 80%,rgba(74,34,120,0) 100%)"></div>
  <h2>What Our User Says</h2>
  <blockquote>“ Nemo enim ipsam voluptatem quia voluptas sit aspernatur aut&nbsp; odit aut fugit, sed quia consequuntur magni dolores porro quisquam est, qui dolorem ipsum quia dolor sit amet, consectetur, adipisci velit..”</blockquote>
  <cite>Name Heading</cite>
</section>
<a class="btn" href="#" style="left:617px;top:3448px;width:254px;height:56px">View All Reviews</a>
<div class="doodle" style="left:410px;top:3550px;width:100px;height:90px;background:var(--red)" role="img" aria-label="Star doodle"></div>
<div class="doodle" style="left:1070px;top:3555px;width:100px;height:90px;background:var(--yellow)" role="img" aria-label="Light bulb doodle"></div>

<!-- Blog -->
<h2 class="abs display" style="left:74px;top:3674px;font-size:44px;color:var(--ink)">Blog Posts</h2>
<article class="post" style="left:74px">
  <div class="photo" role="img" aria-label="Row of children seated with hands raised before a colourful wall" style="background:linear-gradient(135deg,#e4dccf,#c9b79f,#6a88b0)"></div>
  <h3>Nemo enim ipsam voluptatem</h3>
  <p>Nemo enim ipsam voluptatem quia voluptas sit aspernatur aut odit aut fugit, sed quia conse quuntur magni dolores.</p>
</article>
<article class="post" style="left:435px">
  <div class="photo" role="img" aria-label="Girl pointing at an interactive whiteboard" style="background:linear-gradient(135deg,#cfd9e3,#8fb0cc,#e8e2d6)"></div>
  <h3>Nemo enim ipsam voluptatem</h3>
  <p>Nemo enim ipsam voluptatem quia voluptas sit aspernatur aut odit aut fugit, sed quia conse quuntur magni dolores.</p>
</article>
<article class="post" style="left:797px">
  <div class="photo" role="img" aria-label="Children dancing with an instructor in a school gym" style="background:linear-gradient(135deg,#6a5a8a,#c24a3a,#e0d2c0)"></div>
  <h3>Nemo enim ipsam voluptatem</h3>
  <p>Nemo enim ipsam voluptatem quia voluptas sit aspernatur aut odit aut fugit, sed quia conse quuntur magni dolores.</p>
</article>
<div class="doodle" style="left:14px;top:4110px;width:60px;height:70px;border-radius:12px;background:var(--purple)" role="img" aria-label="Music note doodle"></div>

<!-- CTA -->
<section class="cta">
  <h2>Bring Novaflickerium to<br>your school</h2>
  <p>Nemo enim ipsam voluptatem quia voluptas sit&nbsp; aspernatur aut&nbsp; odit aut fugit, sed quia cons equuntur magni dolores porro quisquam est, qui dolorem.</p>
  <div class="doodle" style="left:1108px;top:140px;width:64px;height:80px;border:7px solid var(--orange);background:none" role="img" aria-label="Swirl doodle"></div>
</section>
<a class="btn" href="#" style="left:495px;top:4466px;width:209px;height:58px">Book a Demo</a>
<div class="doodle" style="left:742px;top:4575px;width:100px;height:80px;background:var(--red)" role="img" aria-label="Star doodle"></div>
<div class="doodle" style="left:28px;top:4600px;width:66px;height:80px;border:7px solid var(--red);background:none" role="img" aria-label="Swirl doodle"></div>
<div class="doodle" style="left:1110px;top:4620px;width:50px;height:80px;border-radius:12px;background:var(--ink)" role="img" aria-label="Squiggle doodle"></div>

<!-- Footer -->
<footer class="footer">
  <div class="brand" style="left:74px;top:4752px;width:200px;text-align:center;font-size:26px;color:var(--red)">Novaflickerium</div>
  <p class="copyright">Copyright © 2025. Company Name<br>All rights reserved.</p>
  <h4 style="left:575px">Quick Links</h4>
  <ul>
    <li><a href="#">Home</a></li>
    <li><a href="#">About Us</a></li>
    <li><a href="#">Programs</a></li>
    <li><a href="#">Success Stories</a></li>
    <li><a href="#">Blog</a></li>
    <li><a href="#">Contact Us</a></li>
  </ul>
  <h4 style="left:882px">Contact Info</h4>
  <div class="contact">
    <p style="top:4733px">48 Lantern Row, Suite 12,<br>Brightvale, ST 40718</p>
    <p style="top:4800px;color:var(--red)">hello@novaflickerium.example</p>
  </div>
  <div class="social" aria-label="Social media links">
    <span></span><span></span><span></span><span></span><span></span>
  </div>
</footer>

</body>
</html>
```